Advertisement for Marlowen Talent Prize 2019 needed

I am Lobbying for the needs of youngsters in a specific region. This year I am planning the first marlowen talent prize to give young people the chance to present their regional projekts/activities/initiatives and to award them some price money they can use for further activites. This Initiative is not only targeted at young people but also organizations who work with youngsters. Therefore I would need an advertisment we could use to promote this event in newspapers, website and via an E-Mail Campaign. Possibly also on social media, so I am thinking of a Facebook and Instagram Design as well. I uploaded some logos and materials that we are using already. to give you an idea of the colors. The ad should be targeted towards a young audience but also draw the attention of people who work with youngsters. Size MAX. (length x width) 21cm x 7cm
Youngsters age 14-26 yrs
People who work with youngsters (youth organizations, schools, clubs, social workers, municipalities)

```html
<!DOCTYPE html>
<html lang="de">
<head>
<meta charset="utf-8">
<title>Marlowen Talent Prize 2019</title>
<link rel="stylesheet" href="https://fonts.googleapis.com/css2?family=Anton&family=Open+Sans:wdth,wght@75..100,400..800&display=swap">
<style>
  :root {
    --prize-red: #e3141b;
    --prize-green: #5aa72f;
    --ink: #111111;
    --paper: #ffffff;
    --tag-yellow: #ffe600;
    --splash-red: #e53a2a;
    --splash-orange: #f39a1e;
    --splash-yellow: #f7e43a;
    --splash-green: #3fae3a;
    --splash-blue: #2aa6df;
    --splash-indigo: #2d3a9a;
    --splash-violet: #7a3a9c;
  }
  * { box-sizing: border-box; margin: 0; padding: 0; }
  html, body { width: 1200px; height: 400px; overflow: hidden; background: var(--paper); }
  .banner {
    position: relative;
    width: 1200px;
    height: 400px;
    background: var(--paper);
    border: 6px solid var(--ink);
    overflow: hidden;
    font-family: "Open Sans", Arial, sans-serif;
  }
  .banner__title {
    position: absolute;
    left: 24px;
    top: 4px;
    font-family: "Anton", "Impact", sans-serif;
    font-size: 58px;
    line-height: 1;
    letter-spacing: 0.5px;
    color: var(--prize-red);
    text-transform: uppercase;
  }
  .banner__subtitle {
    position: absolute;
    left: 24px;
    top: 70px;
    font-size: 33px;
    font-weight: 600;
    font-stretch: 85%;
    line-height: 1;
    color: var(--prize-green);
  }
  .banner__eligibility {
    position: absolute;
    left: 24px;
    top: 122px;
    font-size: 18.5px;
    font-weight: 700;
    font-stretch: 78%;
    line-height: 1;
    color: var(--ink);
    white-space: nowrap;
  }
  .region-mark {
    position: absolute;
    right: 0;
    top: 0;
    width: 330px;
    height: 98px;
    border: 4px solid var(--ink);
    border-top: 0;
    border-right: 0;
    background: var(--paper);
    display: flex;
    align-items: center;
    justify-content: center;
    gap: 10px;
  }
  .region-mark__square {
    width: 14px;
    height: 14px;
    background: var(--ink);
  }
  .region-mark__name {
    font-size: 20px;
    font-weight: 700;
    letter-spacing: 2px;
    color: var(--ink);
    text-transform: uppercase;
  }
  .banner__artwork {
    position: absolute;
    left: 0;
    right: 0;
    top: 150px;
    bottom: 0;
    background: linear-gradient(90deg,
      var(--splash-red) 0%,
      var(--splash-orange) 17%,
      var(--splash-yellow) 33%,
      var(--splash-green) 50%,
      var(--splash-blue) 66%,
      var(--splash-indigo) 82%,
      var(--splash-violet) 100%);
    -webkit-mask-image: linear-gradient(180deg, transparent 0%, #000 30%, #000 80%, transparent 100%);
            mask-image: linear-gradient(180deg, transparent 0%, #000 30%, #000 80%, transparent 100%);
    opacity: 0.85;
  }
  .event-date {
    position: absolute;
    left: 0;
    bottom: 0;
    width: 620px;
    height: 46px;
  }
  .event-date svg { position: absolute; inset: 0; }
  .event-date__text {
    position: absolute;
    left: 12px;
    top: 0;
    height: 46px;
    display: flex;
    align-items: center;
    font-size: 25px;
    font-weight: 800;
    font-stretch: 75%;
    color: var(--tag-yellow);
    white-space: nowrap;
  }
</style>
</head>
<body>
  <div class="banner">
    <h1 class="banner__title">Marlowen Talent Prize 2019</h1>
    <p class="banner__subtitle">ein regionaler Preis für innovative Jugendprojekte</p>
    <p class="banner__eligibility">einreichen können Jugendliche zwischen 12 und 26 Jahren, VertreterInnen von Gemeinden, Institutionen, Verbänden und Vereinen</p>

    <div class="region-mark">
      <span class="region-mark__square"></span>
      <span class="region-mark__name">Hügelland Marlowen</span>
    </div>

    <div class="banner__artwork" role="img" aria-label="Bunte Farbspritzer in Regenbogenfarben mit Silhouetten springender, jubelnder Jugendlicher"></div>

    <div class="event-date">
      <svg width="620" height="46" viewBox="0 0 620 46" aria-hidden="true">
        <polygon points="0,0 590,0 620,46 0,46" fill="var(--prize-red)"/>
      </svg>
      <p class="event-date__text">Donnerstag, 19. September&nbsp;&nbsp;|&nbsp;&nbsp;von 17:00 - 20:00 Uhr</p>
    </div>
  </div>
</body>
</html>
```